Etiketten für selbst erzeugten Obstbrand und Liköre
Zielgruppe
Freunde und Bekannte
Aufgabenstellung
Die Etiketten kommen auf Flaschen, die selbst erzeugten Obstbrand und Liköre enthalten. Das Etikett sollte modern, ohne Schnickschnack und edel aussehen. Das Etikett sollte nur aus grafischen Elementen und Schrift bestehen (keine Bilder/Fotos). Die Schnapssorte selbst trage ich auf einem reservierten Feld handschriftlich auf dem Etikett ein. Es sollte maximal 7cm hoch und 10cm breit sein. Die Flaschen werden ausschließlich verschenkt.

```html
<!DOCTYPE html>
<html lang="de">
<head>
<meta charset="UTF-8">
<title>Etikett – Feinster aus Handarbeit</title>
<link href="https://fonts.googleapis.com/css2?family=Great+Vibes&display=swap" rel="stylesheet">
<style>
  :root {
    --page-bg: #f4f4f4;
    --label-bg: #3b3b3b;
    --gold: #c9a85e;
    --write-line: #ffffff;
    --label-shadow: rgba(0, 0, 0, 0.28);
  }
  * { margin: 0; padding: 0; box-sizing: border-box; }
  html, body {
    width: 675px;
    height: 1200px;
    overflow: hidden;
    background: var(--page-bg);
  }
  .canvas {
    width: 675px;
    height: 1200px;
    display: flex;
    align-items: center;
    justify-content: center;
  }
  .label {
    width: 600px;
    height: 419px;
    background: var(--label-bg);
    box-shadow: 8px 10px 18px var(--label-shadow);
  }
  .label svg { display: block; width: 100%; height: 100%; }
  .frame, .diamond { fill: none; stroke: var(--gold); }
  .frame { stroke-width: 4; }
  .diamond { stroke-width: 2; }
  .write-line { stroke: var(--write-line); stroke-width: 3; }
  .fill-line { stroke: var(--gold); stroke-width: 1; opacity: 0.5; }
  .script {
    font-family: 'Great Vibes', cursive;
    fill: var(--gold);
  }
  .title { font-size: 66px; }
  .footer { font-size: 36px; }
</style>
</head>
<body>
<main class="canvas">
  <section class="label">
    <svg viewBox="0 0 930 650" xmlns="http://www.w3.org/2000/svg">
      <rect class="frame" x="31" y="27" width="870" height="588"/>

      <text class="script title" x="465" y="100" text-anchor="middle">Feinster</text>

      <polygon class="diamond" points="465,106 856,348 465,556 80,342"/>
      <polygon class="diamond" points="465,128 820,350 465,536 117,346"/>

      <line class="write-line" x1="192" y1="369" x2="744" y2="369"/>

      <line class="fill-line" x1="42" y1="596" x2="82" y2="596"/>
      <text class="script footer" x="88" y="594">ml</text>

      <text class="script footer" x="465" y="594" text-anchor="middle">aus Handarbeit</text>

      <line class="fill-line" x1="746" y1="596" x2="788" y2="596"/>
      <text class="script footer" x="790" y="594">% Vol.</text>
    </svg>
  </section>
</main>
</body>
</html>
```